Rising Paths Web Design

I am starting a new company that will provide LIFE COACHING services - I have tried to design a website, but it's too complicated. Right now, it's just me - I'm the only person that will provide services through the website - I have used artmarket to purchase a logo (see below). I want to be able to update the website myself, but need a template - basic design. Because I am not technologically savvy enough to explain in words - I basically want to have a website that will provide basic information about my services (coaching), a page about me and my background, hopefully scheduling possibilities, and testimonials — also a page for writing/blogs. I bought a website through NetHarbor - so when I have a template, I guess I”d use that - but maybe I’ll need to work with a designer to actually get it up on the internet. I have a head shot that I’ll upload, too.
Target Market(s)
Clients from the independent (private school) world - teachers, administrators
Number of Pages Required
4 page
Look and feel
Each slider illustrates characteristics of the customer's brand and the style your logo design should communicate.

```html
<!DOCTYPE html>
<html lang="en">
<head>
<meta charset="utf-8">
<title>Rising Paths Coaching</title>
<link rel="stylesheet" href="https://fonts.googleapis.com/css2?family=Cinzel:wght@400;500;600&family=Roboto:wght@400;500;700&display=swap">
<style>
:root{
  --teal:#1a9886;
  --teal-dark:#127a6c;
  --ink:#2b2b2b;
  --grey:#8a8a8a;
  --muted:#a3a3a3;
  --soft:#f2f2f2;
  --dark:#2a2a2a;
  --darker:#1f1f1f;
  --white:#ffffff;
  --gold:#f2a81d;
}
*{box-sizing:border-box;margin:0;padding:0}
html,body{width:1200px;height:4435px;overflow:hidden;background:var(--white)}
body{position:relative;font-family:"Roboto",Arial,sans-serif;color:var(--ink)}
.abs{position:absolute}
.serif{font-family:"Cinzel",Georgia,serif}
.btn{position:absolute;display:flex;align-items:center;justify-content:center;background:var(--teal);color:var(--white);font-weight:700;font-size:14px;border-radius:0 14px 0 14px;letter-spacing:.2px}
.photo{position:absolute}
.section-title{position:absolute;left:0;width:1200px;text-align:center;font-family:"Cinzel",Georgia,serif;font-size:38px;font-weight:500;color:var(--ink);letter-spacing:1px}
.section-title span{color:var(--grey)}
.title-rule{position:absolute;left:553px;width:94px;height:3px;background:var(--teal)}

/* top bar */
.topbar{left:0;top:0;width:1200px;height:43px;background:var(--dark)}
.topbar .social-strip{left:0;top:0;width:358px;height:43px;background:var(--teal)}
.dot-icon{position:absolute;width:30px;height:30px;border-radius:50%;background:var(--white)}
.topbar .contact{position:absolute;top:12px;font-size:14px;color:#e9e9e9}

/* header */
.header{left:0;top:43px;width:1200px;height:100px;background:var(--white)}
.logo-badge{position:absolute;left:95px;top:20px;width:190px;height:170px;border-radius:50%;background:var(--white);z-index:3}
.logo-ring{position:absolute;left:122px;top:52px;width:136px;height:136px;border-radius:50%;border:2px solid var(--teal);z-index:4}
.logo-name{position:absolute;left:95px;top:102px;width:190px;text-align:center;font-family:"Cinzel",Georgia,serif;font-size:16px;color:#444;z-index:5}
.nav a{position:absolute;top:82px;font-size:14px;font-weight:700;color:var(--ink);text-decoration:none}
.nav a.active{color:var(--teal)}

/* hero */
.hero{left:0;top:143px;width:1200px;height:680px;overflow:hidden}
.hero-title{left:141px;top:318px;font-family:"Cinzel",Georgia,serif;font-size:44px;line-height:46px;color:#333;letter-spacing:2px}
.hero-title .accent{color:var(--teal)}
.hero-text{left:111px;top:430px;font-size:18px;line-height:29px;color:#2a2a2a}
.arrow-btn{position:absolute;width:38px;height:38px;border-radius:50%;background:var(--white);display:flex;align-items:center;justify-content:center}

/* about */
.about-text{left:634px;top:988px;width:455px;font-size:14px;line-height:26px;color:var(--muted);text-align:justify}

/* services */
.services-bg{left:0;top:1378px;width:1200px;height:645px;background:var(--soft)}
.card{position:absolute;width:308px;height:429px;background:var(--white);border-radius:0 0 18px 0;box-shadow:0 4px 14px rgba(0,0,0,.10)}
.card.featured{background:var(--teal);border-radius:18px 0 18px 0}
.card .pic{position:absolute;left:7px;top:7px;width:294px;height:208px}
.card h3{position:absolute;left:0;top:235px;width:308px;text-align:center;font-size:19px;font-weight:500;color:var(--ink)}
.card .rule{position:absolute;left:126px;top:263px;width:56px;height:3px;background:var(--teal)}
.card p{position:absolute;left:16px;top:280px;width:276px;text-align:center;font-size:13.5px;line-height:25px;color:var(--muted)}
.card.featured h3,.card.featured p{color:var(--white)}
.card.featured .rule{background:var(--white)}
.card .btn{left:95px;top:365px;width:117px;height:41px;font-size:12px}
.card.featured .btn{background:var(--white);color:var(--ink)}

/* approach */
.approach-circle{left:688px;top:2081px;width:400px;height:400px;border-radius:50%;background:rgba(255,255,255,.95)}
.approach-title{left:688px;top:2155px;width:400px;text-align:center;font-family:"Cinzel",Georgia,serif;font-size:30px;color:var(--ink)}
.approach-title span{color:var(--grey)}
.approach-text{left:714px;top:2228px;width:348px;text-align:center;font-size:13.5px;line-height:26px;color:var(--muted)}

/* testimonials */
.quote-text{left:396px;top:2753px;width:670px;font-size:14px;line-height:26px;color:var(--grey)}
.quote-name{left:396px;top:2841px;font-size:16px;font-weight:700;color:var(--teal)}
.quote-name span{font-size:13px;color:var(--ink);font-weight:500}
.stars{left:396px;top:2866px;font-size:13px;color:var(--gold);letter-spacing:2px}

/* blog */
.blog-bg{left:0;top:2970px;width:1200px;height:671px;background:var(--soft)}
.post{position:absolute;top:3128px;width:308px;height:438px;background:var(--white);border-radius:0 0 18px 0;box-shadow:0 4px 14px rgba(0,0,0,.10)}
.post .pic{position:absolute;left:7px;top:7px;width:294px;height:210px}
.post h3{position:absolute;left:14px;top:238px;width:284px;font-size:19px;line-height:26px;font-weight:500;color:var(--ink)}
.post p{position:absolute;left:14px;top:296px;width:284px;font-size:13.5px;line-height:24px;color:var(--muted)}
.post .avatar{position:absolute;left:14px;top:382px;width:50px;height:50px;border-radius:50%;background:linear-gradient(135deg,#c89b76,#8a5e3f)}
.post .author{position:absolute;left:82px;top:387px;font-size:13.5px;color:var(--ink)}
.post .place{position:absolute;left:82px;top:409px;font-size:11px;color:var(--muted)}

/* appointment */
.book-bg{left:0;top:3641px;width:1200px;height:460px;background:linear-gradient(180deg,#1f9685,#168575)}
.book-title{left:0;top:3688px;width:1200px;text-align:center;font-family:"Cinzel",Georgia,serif;font-size:38px;color:var(--white);letter-spacing:1px}
.book-text{left:130px;top:3768px;width:940px;text-align:center;font-size:14px;line-height:26px;color:#e9f6f3}

/* footer */
.foot-head{position:absolute;top:4130px;font-size:16px;font-weight:700;color:var(--white)}
.foot-rule{position:absolute;top:4156px;width:30px;height:3px;background:var(--teal)}
.foot-item{position:absolute;font-size:14.5px;line-height:21px;color:#e2e2e2}
.copyright{left:0;top:4373px;width:1200px;height:62px;background:var(--darker);color:#d4d4d4;font-size:12.5px;text-align:center;line-height:62px}
</style>
</head>
<body>

<!-- top bar -->
<div class="abs topbar">
  <div class="abs social-strip">
    <span class="dot-icon" style="left:113px;top:6px" aria-label="Social link"></span>
    <span class="dot-icon" style="left:155px;top:6px" aria-label="Social link"></span>
    <span class="dot-icon" style="left:197px;top:6px" aria-label="Social link"></span>
    <span class="dot-icon" style="left:239px;top:6px" aria-label="Social link"></span>
  </div>
  <svg class="abs" style="left:740px;top:14px" width="14" height="14" viewBox="0 0 24 24"><path fill="#1a9886" d="M6.6 10.8c1.4 2.8 3.8 5.1 6.6 6.6l2.2-2.2c.3-.3.7-.4 1-.2 1.1.4 2.3.6 3.6.6.6 0 1 .4 1 1V20c0 .6-.4 1-1 1C10.6 21 3 13.4 3 4c0-.6.4-1 1-1h3.5c.6 0 1 .4 1 1 0 1.2.2 2.4.6 3.6.1.3 0 .7-.2 1l-2.3 2.2z"/></svg>
  <span class="contact" style="left:763px">+1 (555) 010 2040</span>
  <span class="contact" style="left:892px;color:#888">|</span>
  <svg class="abs" style="left:912px;top:15px" width="15" height="12" viewBox="0 0 24 18"><rect width="24" height="18" rx="2" fill="#1a9886"/><path d="M1 2l11 8 11-8" stroke="#2a2a2a" stroke-width="2" fill="none"/></svg>
  <span class="contact" style="left:936px">info@risingpaths.com</span>
</div>

<!-- header -->
<div class="abs header">
  <nav class="nav">
    <a class="active" style="left:467px;top:39px">HOME</a>
    <a style="left:541px;top:39px">ABOUT ME</a>
    <a style="left:645px;top:39px">SERVICES</a>
    <a style="left:745px;top:39px">BLOG</a>
    <a style="left:814px;top:39px">CONTACT</a>
  </nav>
  <div class="abs" style="left:467px;top:57px;width:41px;height:2px;background:var(--teal)"></div>
  <div class="btn" style="left:931px;top:22px;width:157px;height:49px">SCHEDULE NOW</div>
</div>

<!-- hero -->
<div class="abs hero">
  <div class="photo" role="img" aria-label="Woman in a sun hat raising her arms on a hillside at sunset" style="left:0;top:0;width:1200px;height:680px;background:radial-gradient(circle at 72% 25%,#fff1c9 0%,#f3b766 22%,#d4822f 48%,#8e4a1d 78%,#5a2d12 100%)"></div>
  <div class="photo" style="left:0;top:0;width:720px;height:680px;background:linear-gradient(90deg,rgba(255,240,215,.55),rgba(255,240,215,0))"></div>
  <svg class="abs" style="left:0;top:0" width="1200" height="680" viewBox="0 0 1200 680">
    <path d="M0 560 C160 520 300 540 430 540 C620 540 700 700 960 660 C1080 640 1150 600 1200 560 L1200 680 L0 680 Z" fill="#ffffff"/>
    <path d="M0 555 C160 520 300 525 430 530 C620 535 720 680 960 645 C1080 625 1150 590 1200 555" stroke="#1a9886" stroke-width="16" fill="none"/>
  </svg>
</div>
<div class="abs" style="left:111px;top:327px;width:3px;height:78px;background:var(--teal)"></div>
<div class="abs hero-title">RISING PATHS<br><span class="accent">COACHING</span></div>
<div class="abs hero-text">Lorem ipsum dolor sit amet consectetur adipiscing<br>elitmoctetur tempor incididunt.</div>
<div class="btn" style="left:112px;top:503px;width:143px;height:48px">GET STARTED</div>
<div class="arrow-btn" style="left:1006px;top:664px"><svg width="12" height="12" viewBox="0 0 12 12"><path d="M8 1L3 6l5 5" stroke="#333" stroke-width="2" fill="none"/></svg></div>
<div class="arrow-btn" style="left:1050px;top:664px"><svg width="12" height="12" viewBox="0 0 12 12"><path d="M4 1l5 5-5 5" stroke="#333" stroke-width="2" fill="none"/></svg></div>

<!-- logo -->
<div class="logo-badge"></div>
<div class="logo-ring"></div>
<div class="logo-name">RISING PATHS</div>

<!-- about -->
<svg class="abs" style="left:100px;top:835px" width="460" height="470" viewBox="0 0 460 470">
  <circle cx="227" cy="232" r="215" fill="none" stroke="#1a9886" stroke-width="3"/>
</svg>
<div class="photo" role="img" aria-label="Coach with red hair seated in a bright office" style="left:130px;top:890px;width:406px;height:390px;border-radius:50%;background:linear-gradient(135deg,#f1ece6,#d8c7b8 45%,#8b5a3c 70%,#3b2d2a)"></div>
<div class="abs" style="left:382px;top:1122px;width:156px;height:156px;border-radius:50%;background:var(--teal)"></div>
<div class="photo" role="img" aria-label="Coaching session between two people" style="left:389px;top:1129px;width:142px;height:142px;border-radius:50%;background:linear-gradient(135deg,#cfd6da,#7b8790 55%,#2e3439);border:4px solid #fff"></div>
<div class="abs" style="left:635px;top:925px;width:3px;height:34px;background:var(--teal)"></div>
<div class="abs serif" style="left:661px;top:918px;font-size:42px;color:var(--ink);letter-spacing:1px">ABOUT <span style="color:var(--grey)">ME</span></div>
<p class="abs about-text">Lorem ipsum dolor sit amet, consectetur adipiscing elit, sed do eiusmod tempor incididunt ut labore et dolore magna aliqua. Ut enim ad minim veniam, quis nostrud exercitation ullamco laboris nisi ut aliquip ex ea commodo consequat duis aute irure dolor in reprehenderit in voluptenim ad minim veniam quis nostrud exer citation ate velit essnostrud exercitationea.</p>
<div class="btn" style="left:634px;top:1178px;width:137px;height:47px">LEARN MORE</div>

<!-- services -->
<div class="abs services-bg"></div>
<div class="section-title" style="top:1434px">MY <span>SERVICES</span></div>
<div class="title-rule" style="top:1486px"></div>

<div class="card" style="left:112px;top:1529px">
  <div class="pic" role="img" aria-label="Group coaching circle in a warm room" style="background:linear-gradient(135deg,#a57b58,#5b3f2d 50%,#d7c3a9)"></div>
  <h3>LOREM IPSUM DOL</h3><div class="rule"></div>
  <p>Sed ut perspiciatis unde omnis iste nat us error sit voluptatem accusantium dol oremque laudantiumea.</p>
  <div class="btn">LEARN MORE</div>
</div>
<div class="card featured" style="left:446px;top:1529px">
  <div class="pic" role="img" aria-label="Two older friends embracing in a sunny meadow" style="background:linear-gradient(180deg,#f3e2a9,#9cb35a 50%,#3f6f2f)"></div>
  <h3>LOREM IPSUM DOL</h3><div class="rule"></div>
  <p>Sed ut perspiciatis unde omnis iste nat us error sit voluptatem accusantium dol oremque laudantiumea.</p>
  <div class="btn">LEARN MORE</div>
</div>
<div class="card" style="left:780px;top:1529px">
  <div class="pic" role="img" aria-label="Support group talking together indoors" style="background:linear-gradient(135deg,#e5e2dd,#8b7a6d 50%,#3f4a55)"></div>
  <h3>LOREM IPSUM DOL</h3><div class="rule"></div>
  <p>Sed ut perspiciatis unde omnis iste nat us error sit voluptatem accusantium dol oremque laudantiumea.</p>
  <div class="btn">LEARN MORE</div>
</div>

<!-- approach -->
<div class="photo" role="img" aria-label="Two women smiling in conversation at an office desk" style="left:0;top:2023px;width:1200px;height:515px;background:linear-gradient(90deg,#5e6b70,#c9c2bb 28%,#8d7f75 50%,#e2e7ea 75%,#b8c4c9)"></div>
<div class="abs approach-circle"></div>
<div class="abs approach-title">MY <span>APPROACH</span></div>
<p class="abs approach-text">Lorem ipsum dolor sit amet consectetur adipiscing elit, sed do eiusmod tempor incididunt ut labore et dolore magna aliqua. Ut enim ad minim veniam, quis nostrud exercitati lamcoea.</p>
<div class="btn" style="left:825px;top:2364px;width:127px;height:48px">APPLY NOW</div>

<!-- testimonials -->
<div class="section-title" style="top:2618px">TESTIMONIALS</div>
<div class="title-rule" style="top:2668px"></div>
<div class="arrow-btn" style="left:1006px;top:2622px;border:2px solid var(--teal)"><svg width="12" height="12" viewBox="0 0 12 12"><path d="M8 1L3 6l5 5" stroke="#1a9886" stroke-width="2" fill="none"/></svg></div>
<div class="arrow-btn" style="left:1050px;top:2622px;background:var(--teal)"><svg width="12" height="12" viewBox="0 0 12 12"><path d="M4 1l5 5-5 5" stroke="#fff" stroke-width="2" fill="none"/></svg></div>
<svg class="abs" style="left:140px;top:2707px" width="192" height="192" viewBox="0 0 192 192"><circle cx="96" cy="96" r="92" fill="none" stroke="#1a9886" stroke-width="2.5"/></svg>
<div class="photo" role="img" aria-label="Client portrait" style="left:153px;top:2720px;width:166px;height:166px;border-radius:50%;background:linear-gradient(135deg,#e8e8e8,#b08a6d 55%,#4d5a66)"></div>
<svg class="abs" style="left:396px;top:2719px" width="30" height="24" viewBox="0 0 30 24"><path fill="#1a9886" d="M0 24V13C0 5 4 1 11 0v5c-3 1-5 3-5 7h5v12zM17 24V13c0-8 4-12 11-13v5c-3 1-5 3-5 7h5v12z"/></svg>
<p class="abs quote-text">Sed ut perspiciatis unde omnis iste natus error sit voluptatem accusantium doloremque laudantium, totam rem aperiam, eaque ipsa quae ab illo inventore veritatis et quasi architecto beatae vitae dicta sunt explicabo. Nemo enim ipsam voluptatem quia voluptasea.</p>
<div class="abs quote-name">- DANIEL REYES, <span>United States</span></div>
<div class="abs stars">★★★★★</div>

<!-- blog -->
<div class="abs blog-bg"></div>
<div class="section-title" style="top:3033px">LATEST <span>BLOG</span></div>
<div class="title-rule" style="top:3084px"></div>

<div class="post" style="left:112px">
  <div class="pic" role="img" aria-label="Two women stretching outdoors among trees" style="background:linear-gradient(160deg,#f4efd5,#a8b874 50%,#5d7a3c)"></div>
  <h3>Lorem ipsum dolor sit ametcon sectetur adipisea</h3>
  <p>Sed ut perspiciatis unde omnis iste nat us error sit voluptatem accusantium dol orem que laudantiupi ciatmea.</p>
  <div class="avatar" role="img" aria-label="Author portrait"></div>
  <div class="author"><span style="color:var(--teal)">●</span> Maya Collins</div>
  <div class="place">United States</div>
</div>
<div class="post" style="left:446px">
  <div class="pic" role="img" aria-label="Counsellor listening to a client in a bright room" style="background:linear-gradient(135deg,#f1f3f4,#bfc7cc 45%,#6e5849)"></div>
  <h3>Lorem ipsum dolor sit ametcon sectetur adipisea</h3>
  <p>Sed ut perspiciatis unde omnis iste nat us error sit voluptatem accusantium dol orem que laudantiupi ciatmea.</p>
  <div class="avatar" role="img" aria-label="Author portrait"></div>
  <div class="author"><span style="color:var(--teal)">●</span> Maya Collins</div>
  <div class="place">United States</div>
</div>
<div class="post" style="left:780px">
  <div class="pic" role="img" aria-label="Woman walking in tall grass at sunset" style="background:linear-gradient(180deg,#f7c98a,#c47b3b 50%,#3b2a20)"></div>
  <h3>Lorem ipsum dolor sit ametcon sectetur adipisea</h3>
  <p>Sed ut perspiciatis unde omnis iste nat us error sit voluptatem accusantium dol orem que laudantiupi ciatmea.</p>
  <div class="avatar" role="img" aria-label="Author portrait"></div>
  <div class="author"><span style="color:var(--teal)">●</span> Maya Collins</div>
  <div class="place">United States</div>
</div>

<!-- appointment -->
<div class="abs book-bg" role="img" aria-label="Teal tinted landscape backdrop"></div>
<div class="abs book-title">BOOK AN APPOINTMENT</div>
<div class="abs" style="left:553px;top:3738px;width:94px;height:3px;background:var(--white)"></div>
<p class="abs book-text">Lorem ipsum dolor sit amet, consectetur adipiscing elit, sed do eiusmod tempor incididunt ut labore et dolore magna aliqua. Ut enim ad minim veniam, quis nostrud exercitation ullamco laboris nisi ut aliquip ex ea commodo consequat duis aute irure dolor in reprehenderit in voluptenim quis nostrud exer citation ate velit essnostrud exercitationea.</p>
<div class="btn" style="left:522px;top:3875px;width:156px;height:47px;background:var(--white);color:var(--ink)">SCHEDULE NOW</div>

<!-- footer -->
<svg class="abs" style="left:0;top:3960px" width="1200" height="415" viewBox="0 0 1200 415">
  <path d="M0 90 C180 20 360 40 560 110 C760 180 980 130 1200 20 L1200 415 L0 415 Z" fill="#2a2a2a"/>
  <path d="M0 92 C180 24 360 44 560 113 C760 182 980 132 1200 24" stroke="#ffffff" stroke-width="9" fill="none"/>
</svg>
<div class="abs" style="left:112px;top:4143px;width:144px;height:144px;border-radius:50%;border:2px solid #ddd"></div>
<div class="abs serif" style="left:104px;top:4205px;width:160px;text-align:center;font-size:15px;color:var(--white)">RISING PATHS</div>

<div class="foot-head" style="left:351px">NAVIGATION</div><div class="foot-rule" style="left:351px"></div>
<div class="foot-item" style="left:351px;top:4177px"><span style="color:var(--teal)">⊙</span>&nbsp;&nbsp;&nbsp;Home</div>
<div class="foot-item" style="left:351px;top:4215px"><span style="color:var(--teal)">⊙</span>&nbsp;&nbsp;&nbsp;About Me</div>
<div class="foot-item" style="left:351px;top:4253px"><span style="color:var(--teal)">⊙</span>&nbsp;&nbsp;&nbsp;Services</div>
<div class="foot-item" style="left:351px;top:4291px"><span style="color:var(--teal)">⊙</span>&nbsp;&nbsp;&nbsp;Blog</div>
<div class="foot-item" style="left:351px;top:4329px"><span style="color:var(--teal)">⊙</span>&nbsp;&nbsp;&nbsp;Contact</div>

<div class="foot-head" style="left:525px">CONTACT</div><div class="foot-rule" style="left:525px"></div>
<svg class="abs" style="left:525px;top:4180px" width="12" height="16" viewBox="0 0 12 16"><path fill="#1a9886" d="M6 0a6 6 0 0 0-6 6c0 4.5 6 10 6 10s6-5.5 6-10a6 6 0 0 0-6-6zm0 8.5A2.5 2.5 0 1 1 6 3.5a2.5 2.5 0 0 1 0 5z"/></svg>
<div class="foot-item" style="left:557px;top:4177px">456, Lorum Ipsum Dol,<br>United States</div>
<svg class="abs" style="left:525px;top:4227px" width="14" height="14" viewBox="0 0 24 24"><path fill="#1a9886" d="M6.6 10.8c1.4 2.8 3.8 5.1 6.6 6.6l2.2-2.2c.3-.3.7-.4 1-.2 1.1.4 2.3.6 3.6.6.6 0 1 .4 1 1V20c0 .6-.4 1-1 1C10.6 21 3 13.4 3 4c0-.6.4-1 1-1h3.5c.6 0 1 .4 1 1 0 1.2.2 2.4.6 3.6.1.3 0 .7-.2 1l-2.3 2.2z"/></svg>
<div class="foot-item" style="left:557px;top:4224px">+1 (555) 010 2040</div>
<svg class="abs" style="left:525px;top:4261px" width="14" height="14" viewBox="0 0 14 14"><rect x="1" y="4" width="12" height="9" rx="1" fill="#1a9886"/><rect x="3" y="1" width="8" height="4" fill="#1a9886"/></svg>
<div class="foot-item" style="left:557px;top:4258px">+1 (555) 010 2041</div>
<svg class="abs" style="left:525px;top:4296px" width="15" height="12" viewBox="0 0 24 18"><rect width="24" height="18" rx="2" fill="#1a9886"/><path d="M1 2l11 8 11-8" stroke="#2a2a2a" stroke-width="2" fill="none"/></svg>
<div class="foot-item" style="left:557px;top:4292px">info@risingpaths.com</div>

<div class="foot-head" style="left:778px">SIGN UP NEWSLETTER</div><div class="foot-rule" style="left:778px"></div>
<div class="abs" style="left:780px;top:4182px;width:308px;height:48px;background:var(--white);border-radius:0 0 14px 0"></div>
<div class="abs" style="left:796px;top:4198px;font-size:14px;color:#555">Email Address</div>
<svg class="abs" style="left:1054px;top:4197px" width="18" height="18" viewBox="0 0 24 24"><path d="M2 12L22 2 16 22l-4-8z" stroke="#1a9886" stroke-width="2" fill="none"/></svg>
<span class="dot-icon" style="left:780px;top:4252px;width:34px;height:34px;background:var(--teal)" aria-label="Social link"></span>
<span class="dot-icon" style="left:823px;top:4252px;width:34px;height:34px" aria-label="Social link"></span>
<span class="dot-icon" style="left:866px;top:4252px;width:34px;height:34px" aria-label="Social link"></span>
<span class="dot-icon" style="left:911px;top:4252px;width:34px;height:34px" aria-label="Social link"></span>

<div class="abs copyright">© 2022 <b>RISING PATHS</b> &nbsp;|&nbsp; All Rights Reserved</div>

</body>
</html>
```